Laundry pickup and delivery flyer "Fold Harbor laundry"

I need a flyer "8.5"x11" that tells customers about our pickup and delivery laundry service. our website address is: www.foldharborlaundry.example The flyer should be front and back.

Font styles to use
Sans Serif

Colors
0094D4
00A9DD
6FCCEA
C7EBF8
E9F6FB

```html
<!DOCTYPE html>
<html lang="en">
<head>
<meta charset="utf-8">
<title>Fold Harbor laundry – pickup and delivery flyer</title>
<link href="https://fonts.googleapis.com/css2?family=Montserrat:wght@300;400;500;600;700;800;900&display=swap" rel="stylesheet">
<style>
  :root{
    --blue:#0094D4;
    --sky:#00A9DD;
    --aqua:#6FCCEA;
    --ice:#C7EBF8;
    --mist:#E9F6FB;
    --navy:#1B5B8C;
    --deep:#1F6BB0;
    --band:#8FD3EE;
    --grey:#6E6E72;
    --text:#3B4A57;
  }
  *{box-sizing:border-box;margin:0;padding:0}
  html,body{width:1200px;height:3350px;overflow:hidden}
  body{background:#F1F2F4;font-family:"Montserrat",sans-serif;color:var(--text);position:relative}
  .page{position:absolute;left:100px;width:1000px;height:1294px;background:#fff;overflow:hidden;box-shadow:0 6px 24px rgba(0,0,0,.12)}
  .page--front{top:280px}
  .page--back{top:1776px}
  .abs{position:absolute}
  .top-bar{left:0;top:0;width:1000px;height:12px;background:var(--deep)}
  .top-tab{left:566px;top:0;width:434px;height:22px;background:var(--sky);clip-path:polygon(4% 0,100% 0,100% 100%,0 100%)}
  .photo{position:absolute}
  .divider-line{left:0;width:1000px;height:8px;background:var(--deep)}

  /* front */
  .hero-photo{left:0;top:22px;width:1000px;height:730px;background:linear-gradient(180deg,#fff 0%,#f7f8f9 45%,#b9b8b6 80%,#8d8c89 100%)}
  .brand{left:650px;top:120px;display:flex;align-items:center;gap:14px}
  .brand__dot{width:44px;height:44px;border-radius:50%;background:var(--blue)}
  .brand__name{font-weight:800;font-size:44px;color:var(--blue);letter-spacing:-.5px}
  .price-badge{left:606px;top:205px;width:370px;height:370px;border-radius:50%;background:var(--navy);border:10px solid var(--aqua);outline:3px solid var(--navy);text-align:center;color:#fff;padding-top:78px}
  .price-badge__label{font-weight:700;font-size:29px;letter-spacing:.5px}
  .price-badge__amount{font-weight:900;font-size:82px;line-height:1.05}
  .price-badge__amount sup{font-size:44px}
  .price-badge__unit{font-weight:900;font-size:58px;color:var(--aqua);line-height:1}
  .van-photo{left:0;top:778px;width:385px;height:200px;background:linear-gradient(90deg,#2f6fb8 0%,#e9eef3 45%,#fdfdfd 70%,#c7ccd1 100%);border-radius:0 40px 20px 0}
  .offer{left:420px;top:770px}
  .offer__big{font-weight:900;font-size:98px;color:var(--navy);line-height:1;letter-spacing:-1px}
  .offer__mid{font-weight:800;font-size:48px;color:var(--blue);line-height:1.15}
  .pill{display:inline-block;border:3px solid var(--navy);border-radius:40px;color:var(--navy);font-weight:800}
  .offer .pill{margin-top:10px;font-size:34px;padding:4px 24px}
  .how-band{left:0;top:986px;width:1000px;height:162px;background:var(--band)}
  .how-tab{left:330px;top:986px;width:336px;height:36px;background:var(--deep);color:#fff;font-weight:800;font-size:27px;text-align:center;line-height:36px;clip-path:polygon(0 0,100% 0,95% 100%,5% 100%)}
  .steps{left:70px;top:1040px;display:flex;align-items:center;gap:14px}
  .step{display:flex;align-items:center;gap:12px}
  .step p{width:118px;font-size:10.5px;font-weight:600;color:#fff;line-height:1.3}
  .step svg{flex:none}
  .arrow{flex:none}
  .contact{left:80px;top:1172px}
  .contact__label{font-weight:800;font-size:20px;color:var(--deep)}
  .contact__line{font-size:34px;font-weight:400;color:var(--blue);margin-top:6px}
  .contact__line strong{font-weight:800;color:var(--navy);font-size:48px}
  .partner{left:600px;top:1170px}
  .partner__row{display:flex;align-items:center;gap:16px}
  .partner__by{font-size:12px;color:var(--blue);line-height:1.1}
  .partner__by b{display:block;font-size:19px;font-weight:800;color:var(--deep)}
  .partner__sep{width:2px;height:38px;background:var(--grey)}
  .partner__name{display:flex;align-items:center;gap:8px;font-size:22px;font-weight:600;color:#333}
  .partner__name i{width:14px;height:14px;background:#333;display:block}
  .address{display:flex;gap:10px;align-items:flex-start;margin-top:10px;font-size:12px;color:var(--text);line-height:1.35}
  .bottom-band{left:0;top:1270px;width:1000px;height:24px;background:var(--aqua)}
  .bottom-tab{left:760px;top:1264px;width:240px;height:30px;background:var(--deep);clip-path:polygon(6% 0,100% 0,100% 100%,0 100%)}

  /* back */
  .basket-photo{left:0;top:22px;width:1000px;height:418px;background:linear-gradient(90deg,#e6e3df 0%,#c9b8a8 40%,#b9c6cf 60%,#6d7c5a 100%)}
  .col{top:475px}
  .col--left{left:80px;width:410px}
  .col--right{left:545px;width:445px}
  .col__kicker{font-weight:800;font-size:32px;color:var(--blue);line-height:1}
  .col__title{font-weight:800;font-size:32px;color:var(--navy);line-height:1.05}
  .col__body{margin-top:14px;font-size:12.4px;line-height:1.4;color:var(--text)}
  .free-title{left:80px;top:690px;font-weight:900;font-size:52px;line-height:1;color:var(--navy)}
  .free-title span{color:var(--blue);display:block}
  .col-divider{left:506px;top:470px;height:275px;border-left:2px dashed #9aa7b1}
  .van-photo--back{left:0;top:790px;width:492px;height:180px;background:linear-gradient(90deg,#2f6fb8 0%,#e9eef3 40%,#fdfdfd 65%,#c0c6cc 100%);border-radius:0 40px 20px 0}
  .outsource{left:545px;top:704px;width:455px;height:118px;background:var(--mist);padding:14px 20px;border-left:2px dashed #9aa7b1}
  .outsource__lead{font-weight:700;font-size:29px;color:var(--navy);line-height:1.1}
  .outsource__sub{font-weight:400;font-size:29px;color:var(--blue);line-height:1}
  .pricing{left:545px;top:835px}
  .pricing .pill{font-size:22px;padding:1px 18px;border-color:var(--deep);color:var(--deep)}
  .pricing__item{font-weight:800;font-size:38px;color:var(--grey);line-height:1.2;margin-top:4px}
  .pricing__price{font-weight:900;font-size:48px;color:var(--navy);line-height:1.05}
  .why-band{left:0;top:970px;width:680px;height:178px;background:var(--band);clip-path:polygon(0 0,100% 0,94% 100%,0 100%)}
  .why-tab{left:0;top:970px;width:380px;height:42px;background:var(--deep);color:#fff;font-weight:800;font-size:26px;line-height:42px;padding-left:80px;clip-path:polygon(0 0,100% 0,94% 100%,0 100%)}
  .why-list{left:80px;top:1030px;width:520px;list-style:none}
  .why-list li{display:flex;gap:10px;font-size:11.5px;font-weight:600;color:#fff;line-height:1.3;margin-bottom:8px}
  .why-list svg{flex:none;margin-top:1px}
  .sweater-photo{left:640px;top:970px;width:360px;height:190px;background:linear-gradient(180deg,#f2f2f0 0%,#7d7f86 35%,#d99a2b 60%,#3f8f7d 100%);clip-path:polygon(8% 0,100% 0,100% 100%,0 100%)}
</style>
</head>
<body>

<!-- FRONT -->
<section class="page page--front">
  <div class="photo hero-photo" role="img" aria-label="Photo of a woman relaxing on a grey sofa with her phone while colourful laundry floats above her"></div>
  <div class="abs top-bar"></div>
  <div class="abs top-tab"></div>

  <div class="abs brand"><span class="brand__dot"></span><span class="brand__name">Fold Harbor</span></div>

  <div class="abs price-badge">
    <div class="price-badge__label">WASH &amp; FOLD</div>
    <div class="price-badge__amount"><sup>$</sup>1.50</div>
    <div class="price-badge__unit">POUND</div>
  </div>

  <div class="abs divider-line" style="top:752px"></div>

  <div class="photo van-photo" role="img" aria-label="Photo of the white and blue branded delivery van"></div>

  <div class="abs offer">
    <div class="offer__big">GET FREE</div>
    <div class="offer__mid">PICKUP &amp; DELIVERY</div>
    <div class="pill">LAUNDRY SERVICE TODAY</div>
  </div>

  <div class="abs how-band"></div>
  <div class="abs how-tab">HOW IT WORKS</div>

  <div class="abs steps">
    <div class="step">
      <svg width="52" height="52" viewBox="0 0 52 52" fill="none" stroke="#fff" stroke-width="3"><circle cx="26" cy="26" r="22"/><path d="M26 12v14l9 6"/></svg>
      <p>Schedule a pickup here feel free to leave your bag where our driver can get to it.</p>
    </div>
    <svg class="arrow" width="26" height="20" viewBox="0 0 26 20" fill="var(--deep)"><path d="M0 7h14V0l12 10-12 10v-7H0z"/></svg>
    <div class="step">
      <svg width="64" height="40" viewBox="0 0 64 40" fill="none" stroke="#fff" stroke-width="3"><path d="M3 30V8h38l12 10h8v12z"/><circle cx="16" cy="32" r="5"/><circle cx="48" cy="32" r="5"/></svg>
      <p>Our driver will pickup your clothes at the scheduled time.</p>
    </div>
    <svg class="arrow" width="26" height="20" viewBox="0 0 26 20" fill="var(--deep)"><path d="M0 7h14V0l12 10-12 10v-7H0z"/></svg>
    <div class="step">
      <svg width="46" height="52" viewBox="0 0 46 52" fill="#fff"><rect x="2" y="2" width="42" height="48" rx="4"/><circle cx="23" cy="30" r="13" fill="var(--band)"/><circle cx="23" cy="30" r="9" fill="#fff"/><rect x="8" y="7" width="12" height="4" fill="var(--band)"/></svg>
      <p>Your clothes are expertly cleaned by our team of laundry professionals</p>
    </div>
    <svg class="arrow" width="26" height="20" viewBox="0 0 26 20" fill="var(--deep)"><path d="M0 7h14V0l12 10-12 10v-7H0z"/></svg>
    <div class="step">
      <svg width="56" height="44" viewBox="0 0 56 44" fill="none" stroke="#fff" stroke-width="3"><path d="M24 10a4 4 0 1 1 4 4v6L4 34h48L28 20"/><rect x="10" y="34" width="36" height="8" fill="#fff"/></svg>
      <p>We delivery your clean clothes back to you at your convenience.</p>
    </div>
  </div>

  <div class="abs contact">
    <div class="contact__label">CONTACT US</div>
    <div class="contact__line">Call us at <strong>555-214-0386</strong></div>
  </div>

  <div class="abs partner">
    <div class="partner__row">
      <div class="partner__by">POWERED BY<b>BRIGHTLINE</b></div>
      <span class="partner__sep"></span>
      <div class="partner__name"><i></i>BRIGHTLINE</div>
    </div>
    <div class="address">
      <svg width="16" height="22" viewBox="0 0 16 22" fill="var(--navy)"><path d="M8 0a8 8 0 0 0-8 8c0 6 8 14 8 14s8-8 8-14a8 8 0 0 0-8-8zm0 11a3 3 0 1 1 0-6 3 3 0 0 1 0 6z"/></svg>
      <span>1480 Harbor Lane, Suite B, Jackson,<br>MS 39201, United States</span>
    </div>
  </div>

  <div class="abs bottom-band"></div>
  <div class="abs bottom-tab"></div>
</section>

<!-- BACK -->
<section class="page page--back">
  <div class="photo basket-photo" role="img" aria-label="Photo of a person holding a woven basket of neatly folded clothes"></div>
  <div class="abs top-bar"></div>
  <div class="abs top-tab"></div>
  <div class="abs divider-line" style="top:440px"></div>

  <div class="abs col col--left">
    <div class="col__kicker">RESIDENTIAL</div>
    <div class="col__title">DELIVERY SERVICE</div>
    <p class="col__body">Utilize our laundry pickup and delivery service to make laundry day easy. Don't waste your free time doing laundry. Go and do life instead. We pick up your laundry at your doorstep and return it the next day to the same spot. Your professionally cleaned and folded clothes will be delivered back to you ready for the drawer or closet.</p>
  </div>
  <div class="abs free-title">FREE PICKUP<span>AND DELIVERY</span></div>
  <div class="photo van-photo--back" role="img" aria-label="Photo of the branded delivery van with the website www.foldharborlaundry.example"></div>

  <div class="abs col-divider"></div>

  <div class="abs col col--right">
    <div class="col__kicker">COMMERCIAL</div>
    <div class="col__title">LAUNDRY SERVICE</div>
    <p class="col__body">Let us help your business grow by taking the burden of laundry off of you. Our commercial grade washing, highly seasoned process &amp; quality assurances will ensure your business thrives. So invest in your business and send those dirty towels, aprons, bedding or any other washable items that your business needs to be spotless. Gain ROI instantly by selecting Fold Harbor as your cleaning partner against dirt and stains. Focus your time on your business instead.</p>
  </div>

  <div class="abs outsource">
    <div class="outsource__lead">Outsource laundry.</div>
    <div class="outsource__sub">Spend time on what's most important</div>
  </div>

  <div class="abs pricing">
    <div class="pill">PRICING &amp; SERVICES</div>
    <div class="pricing__item">WASH AND FOLD:</div>
    <div class="pricing__price">$1.50/ POUND</div>
  </div>

  <div class="abs why-band"></div>
  <div class="photo sweater-photo" role="img" aria-label="Photo of hands stacking folded knit sweaters in grey, mustard and green"></div>
  <div class="abs why-tab">WHY FOLD HARBOR?</div>
  <ul class="abs why-list">
    <li><svg width="14" height="14" viewBox="0 0 14 14"><circle cx="7" cy="7" r="6.5" fill="var(--deep)"/><path d="M4 7l2 2 4-4" stroke="#fff" stroke-width="1.6" fill="none"/></svg>Our laundry professionals separate lights and darks to keep your clothes looking great.</li>
    <li><svg width="14" height="14" viewBox="0 0 14 14"><circle cx="7" cy="7" r="6.5" fill="var(--deep)"/><path d="M4 7l2 2 4-4" stroke="#fff" stroke-width="1.6" fill="none"/></svg>Your items will never be washed with anyone else's</li>
    <li><svg width="14" height="14" viewBox="0 0 14 14"><circle cx="7" cy="7" r="6.5" fill="var(--deep)"/><path d="M4 7l2 2 4-4" stroke="#fff" stroke-width="1.6" fill="none"/></svg>We use high quality detergents and eco friends chemicals</li>
    <li><svg width="14" height="14" viewBox="0 0 14 14"><circle cx="7" cy="7" r="6.5" fill="var(--deep)"/><path d="M4 7l2 2 4-4" stroke="#fff" stroke-width="1.6" fill="none"/></svg>No more Laundry day</li>
  </ul>

  <div class="abs contact">
    <div class="contact__label">CONTACT US</div>
    <div class="contact__line">Call us at <strong>555-214-0386</strong></div>
  </div>

  <div class="abs partner">
    <div class="partner__row">
      <div class="partner__by">POWERED BY<b>BRIGHTLINE</b></div>
      <span class="partner__sep"></span>
      <div class="partner__name"><i></i>BRIGHTLINE</div>
    </div>
    <div class="address">
      <svg width="16" height="22" viewBox="0 0 16 22" fill="var(--navy)"><path d="M8 0a8 8 0 0 0-8 8c0 6 8 14 8 14s8-8 8-14a8 8 0 0 0-8-8zm0 11a3 3 0 1 1 0-6 3 3 0 0 1 0 6z"/></svg>
      <span>1480 Harbor Lane, Suite B, Jackson,<br>MS 39201, United States</span>
    </div>
  </div>

  <div class="abs bottom-band"></div>
  <div class="abs bottom-tab"></div>
</section>

</body>
</html>
```